Single Splash Web Page as Long Term Placeholder

I registered the url SurfAndSwirl.net. This is the name of a business I will be starting several years down the road. It will be a coffee (drips) and ice cream (dips) store located in a beach town somewhere on the east coast of the US, probably in the Outer Banks of NC. I need a single page that will have the name of the business and the text:

Coming eventually to a beach near you!

The page should somehow reflect the beach environment.

```html
<!DOCTYPE html>
<html lang="en">
<head>
<meta charset="utf-8">
<title>Surf &amp; Swirl</title>
<link rel="stylesheet" href="https://fonts.googleapis.com/css2?family=Oswald:wght@600&family=Pacifico&display=swap">
<style>
  :root {
    --sand: #a4963a;
    --sand-dark: #958830;
    --foam: #8fa9b0;
    --water: #1f5365;
    --water-deep: #173f4f;
    --text: #ffffff;
  }
  html, body {
    margin: 0;
    padding: 0;
    width: 1200px;
    height: 577px;
    overflow: hidden;
    background: var(--sand);
  }
  .splash {
    position: relative;
    width: 1200px;
    height: 577px;
    overflow: hidden;
  }
  .beach-scene {
    position: absolute;
    inset: 0;
    background: linear-gradient(125deg,
      var(--water-deep) 0%,
      var(--water) 32%,
      var(--foam) 50%,
      var(--sand) 64%,
      var(--sand-dark) 100%);
  }
  .brand-name {
    position: absolute;
    left: 0;
    width: 1200px;
    top: 90px;
    margin: 0;
    text-align: center;
    font-family: "Oswald", sans-serif;
    font-weight: 600;
    font-size: 42px;
    line-height: 1.2;
    letter-spacing: 0.5px;
    color: var(--text);
    text-shadow: 2px 3px 4px rgba(0,0,0,0.5);
  }
  .tagline {
    position: absolute;
    left: 0;
    width: 1200px;
    top: 350px;
    margin: 0;
    text-align: center;
    font-family: "Pacifico", cursive;
    font-size: 36px;
    line-height: 1.3;
    color: var(--text);
    text-shadow: 2px 3px 4px rgba(0,0,0,0.5);
  }
</style>
</head>
<body>
<main class="splash">
  <div class="beach-scene" role="img" aria-label="Illustrated beach seen from above: teal sea with a foamy shoreline curving across sandy beach, a faint coffee and ice cream emblem in the water, and a red and white umbrella over a wooden lounge chair on the sand"></div>
  <h1 class="brand-name">SURF &amp; SWIRL</h1>
  <p class="tagline">" Coming eventually to a beach near you! "</p>
</main>
</body>
</html>
```